Webseite für Klempnerei Stolzke GmbH
Zielgruppe
Traditionsreicher Familienbetrieb: Klempnerei für Heizung, Bäder nach Maß und Sanitär, Dachklempnerei, Solar, alternative Energien
Aufgabenstellung
Die Farben der Webseite sollen bitte die gleichen, wie auf der alten Seite sein.
Also blau mit Akzenten in vorwiegend rot und ein wenig gelb.
Insgesamt soll die Webseite klar strukturiert sein, aber dennoch modern wirken.
Die Navigationsleiste bitte in folgender Reihenfolge:
-Start
- Das sind wir
-Leistungsübersicht
- Referenzen
- aktuelle Meldungen
- Kontakt
Die Startseite soll wie folgt gestaltet sein und Call to action wahllos in der Startseite evrteilen:
- großes Headerbild
-Teaser zu' Das sind wir' - Familientradition betonen
- Leistungsübersicht in Boxen mit großem Bild und angedeuteter Verlinkung zu der Leistungsunterseite: Heizung, Bäder nach Maß, Dachklempnerei, Solar, alternative Energien
-Teaser zu Referenzen
- Teaser zu aktuelle Meldungen
- Kontakt mit Map
- Footer mit Aufführung: Mitglied der Innung
-Datenschutz und Impressum
Bei den Inhalten bitte an der alten Webseite orientieren: https://www.heizung-stolzke-beispiel.de/#
Bilder bitte entsprechende Vorschlagen

```html
<!DOCTYPE html>
<html lang="de">
<head>
<meta charset="utf-8">
<title>Klempnerei Stolzke GmbH – Heizung, Sanitär, Bauklempnerei</title>
<link href="https://fonts.googleapis.com/css2?family=Montserrat:wght@400;500;600;700;800&display=swap" rel="stylesheet">
<style>
:root{
  --blue:#3f52a4;
  --blue-dark:#2f3f8a;
  --red:#e2191c;
  --yellow:#f6c400;
  --light:#eceff7;
  --text:#555a66;
  --white:#fff;
}
*{box-sizing:border-box;margin:0;padding:0}
html,body{width:1200px;height:4662px;overflow:hidden}
body{position:relative;font-family:'Montserrat',sans-serif;color:var(--text);background:var(--white)}
.abs{position:absolute}
a{color:inherit}
.topbar{left:0;top:0;width:1200px;height:40px;background:var(--red);color:#fff;font-size:11px;font-weight:600}
.topbar span{position:absolute;top:12px}
.brand{font-weight:800;color:var(--blue);font-size:34px;letter-spacing:-.5px}
.brand-dot{display:inline-block;width:30px;height:30px;border-radius:50%;background:var(--red);vertical-align:-4px;margin-right:8px}
.tagline{font-size:12px;color:var(--blue);font-weight:600}
.hotline{right:87px;top:46px;font-size:31px;font-weight:700;color:var(--blue)}
.notdienst{right:87px;top:88px;font-size:17px;font-weight:600;color:var(--blue)}
.nav{left:0;top:123px;width:1200px;height:53px;background:var(--blue)}
.nav a{position:absolute;top:19px;font-size:13px;font-weight:700;color:#fff;text-decoration:none;text-transform:uppercase}
.nav .active{top:0;left:92px;width:104px;height:53px;background:#fff;color:var(--blue);text-align:center;line-height:53px}
.hero{left:0;top:176px;width:1200px;height:590px;background:linear-gradient(120deg,#9aa2b0,#d9dde3 45%,#7d8594)}
.hero-box{left:0;top:110px;width:700px;height:348px;background:rgba(255,255,255,.82)}
.hero h1{position:absolute;left:85px;top:20px;width:600px;font-size:40px;line-height:49px;font-weight:800;color:var(--blue);text-transform:uppercase}
.hero p{position:absolute;left:89px;top:168px;width:600px;font-size:23px;line-height:29px;color:var(--red)}
.btn{display:block;background:var(--blue);color:#fff;font-weight:700;text-align:center;border-radius:4px;text-decoration:none}
.dot{position:absolute;top:552px;width:42px;height:5px;background:#fff;border-radius:3px}
.about{left:4px;top:824px;width:1192px;height:428px;background:linear-gradient(90deg,#dde1ee,#f4f5fa 60%,#fff);border:1px solid #d6dbe9}
.sec-title{font-size:30px;font-weight:700;color:var(--red);text-transform:uppercase}
.about .sec-title{position:absolute;top:15px;width:100%;text-align:center}
.about h2{position:absolute;top:70px;width:100%;text-align:center;font-size:27px;font-weight:600;color:var(--blue)}
.about .brandwrap{position:absolute;left:146px;top:200px}
.about p{position:absolute;left:505px;width:598px;font-size:15.5px;line-height:20px;text-align:justify}
.services{left:0;top:1309px;width:1200px;height:646px;background:var(--light)}
.underline{height:4px;background:var(--red)}
.services .intro{position:absolute;left:90px;top:153px;width:1030px;font-size:15.5px;line-height:20px}
.card{position:absolute;top:242px;height:359px;background:var(--blue);border-radius:12px;color:#fff;text-align:center}
.card.red{background:var(--red)}
.card svg{margin-top:70px}
.card h3{font-size:21px;font-weight:700;margin-top:14px;line-height:25px}
.card p{font-size:12.5px;line-height:16px;margin:14px 24px 0}
.card .more{position:absolute;left:45px;bottom:20px;font-size:13px;font-weight:700}
.circle-btn{position:absolute;width:26px;height:26px;border-radius:50%;background:var(--blue)}
.ref-band{left:0;top:2054px;width:1200px;height:323px;background:#eef0f6}
.photo{background:linear-gradient(160deg,#c9cedb,#8893b3)}
.ref-text{left:512px;top:2148px;width:590px;font-size:16.5px;line-height:20px}
.partner{position:absolute;top:2410px;height:50px;border-radius:6px;background:#dfe3ee}
.news-card{position:absolute;top:2630px}
.news-card .img{height:251px;background:linear-gradient(150deg,#dfe3ea,#9aa4bd)}
.news-card .meta{margin-top:20px;font-size:12.5px;color:#8a8e98;font-weight:600;word-spacing:2px}
.news-card h3{margin-top:20px;font-size:20.5px;color:var(--red);font-weight:700;line-height:25px}
.news-card p{margin-top:18px;font-size:13.5px;line-height:23px;color:#8a8e98}
.news-card .more{position:absolute;font-size:13px;color:var(--blue);font-weight:700}
.contact{left:0;top:3186px;width:742px;height:434px;background:var(--light)}
.ic{position:absolute;width:44px;height:44px;border-radius:50%;background:var(--blue)}
.lbl{position:absolute;font-size:17px;color:var(--blue)}
.val{position:absolute;font-size:21px;font-weight:700;color:var(--blue)}
.form label{position:absolute;font-size:12px;font-style:italic;color:#555}
.field{position:absolute;height:47px;border:2px solid var(--blue);border-radius:2px;font-size:13px;color:#999;padding:14px 12px;font-style:italic}
.check{position:absolute;width:16px;height:16px;border:1.5px solid #666}
.small{position:absolute;font-size:11.5px;font-style:italic;color:#444;line-height:16px}
.map{left:641px;top:3714px;width:550px;height:617px;background:linear-gradient(135deg,#e6ebe4,#d9e2ee 60%,#eef0e8);border-radius:14px;overflow:hidden}
.footer{left:0;top:4389px;width:1200px;height:273px;background:var(--blue);color:#fff}
.social{position:absolute;top:4425px;width:36px;height:36px;border-radius:6px;background:var(--red)}
.f-h{font-size:13px;font-weight:700}
.f-t{font-size:13.5px;line-height:16px}
</style>
</head>
<body>

<!-- Top bar -->
<div class="abs topbar">
  <span style="left:88px">☎ 03721 480151</span>
  <span style="left:202px">✉ info@heizung-stolzke-beispiel.de</span>
  <span style="left:1006px"><i style="display:inline-block;width:18px;height:12px;background:linear-gradient(#111 33%,#d00 33% 66%,var(--yellow) 66%);border-radius:50%;vertical-align:-2px"></i> DE ▾</span>
</div>

<!-- Header -->
<div class="abs" style="left:97px;top:48px">
  <div class="brand"><span class="brand-dot"></span>Stolzke</div>
  <div class="tagline" style="margin-left:2px">Heizung · Sanitär · Bauklempnerei</div>
</div>
<div class="abs hotline">
  <svg width="28" height="28" viewBox="0 0 24 24" style="vertical-align:-3px"><path fill="#3f52a4" d="M6.6 10.8a15 15 0 0 0 6.6 6.6l2.2-2.2c.3-.3.7-.4 1-.2 1.1.4 2.3.6 3.6.6.6 0 1 .4 1 1V20c0 .6-.4 1-1 1A17 17 0 0 1 3 4c0-.6.4-1 1-1h3.5c.6 0 1 .4 1 1 0 1.3.2 2.5.6 3.6.1.3 0 .7-.2 1z"/></svg>
  03721 480150
</div>
<div class="abs notdienst">24/7 Notdienst</div>

<!-- Navigation -->
<nav class="abs nav">
  <a class="active" href="#">Start</a>
  <a href="#" style="left:237px">Das sind wir</a>
  <a href="#" style="left:389px">Leistungsübersicht</a>
  <a href="#" style="left:603px">Referenzen</a>
  <a href="#" style="left:747px">Aktuelle Meldungen</a>
</nav>

<!-- Hero -->
<section class="abs hero" role="img" aria-label="Foto: Klempner arbeitet an Rohrleitungen unter einem Waschbecken, Werkzeugtasche im Vordergrund">
  <div class="abs hero-box">
    <h1>Ihrem Experten für Heizung, Sanitär und Bauklempnerei</h1>
    <p>Suchen Sie einen Klempner, auf den Sie sich verlassen können? Stolzke, Ihr vertrauenswürdiges lokales Sanitärunternehmen, ist für Sie da!</p>
    <a class="btn abs" href="#" style="left:85px;top:470px;width:347px;height:41px;line-height:41px;font-size:19px">Kontaktiere Uns Jetzt</a>
  </div>
  <i class="dot" style="left:938px"></i><i class="dot" style="left:992px;background:var(--blue)"></i><i class="dot" style="left:1046px"></i>
</section>

<!-- Das sind wir -->
<section class="abs about">
  <div class="sec-title">Das sind wir</div>
  <h2>Stolzke – Ein Meisterbetrieb mit Erfahrung und Tradition</h2>
  <div class="brandwrap">
    <div class="brand" style="font-size:46px"><span class="brand-dot" style="width:40px;height:40px"></span>Stolzke</div>
    <div class="tagline" style="font-size:16px">Heizung · Sanitär · Bauklempnerei</div>
  </div>
  <p style="top:128px">Seit der Gründung im Jahr 1989 ist unser Meisterbetrieb in der Hand von Familie Stolzke. Wir sind Ihre Anlaufstelle für hochwertige und facettenreiche Klempnerarbeiten. Mit einem hohen Fachwissen und einem exzellenten Qualitätsbewusstsein realisieren wir vielfältige Arbeiten im Bereich Heizung und Sanitär. Egal, ob Sie sich für alternative Energien oder Bäder nach Maß interessieren, bei uns erhalten Sie nicht nur eine fachgerechte Durchführung Ihrer Wünsche, sondern auch eine allumfassende Beratung. Unsere 14 kompetenten Mitarbeiter stehen Ihnen während des gesamten Bauprozesses und auch darüber hinaus zur Seite und sind von der Planung bis zur regelmäßigen Wartung der Anlagen für Sie da.</p>
  <p style="top:362px">Seit 01.01.2020 ist die Firma Bernd Stolzke in die Stolzke GmbH umfirmiert.</p>
</section>

<!-- Leistungsübersicht -->
<section class="abs services">
  <div class="sec-title abs" style="left:90px;top:55px">Leistungsübersicht</div>
  <div class="abs underline" style="left:90px;top:98px;width:355px"></div>
  <p class="intro">Unser Leistungsspektrum deckt alle Arbeiten rund um Sanitär, Heizung und Bauklempnerei ab. Bei all unseren Arbeiten orientieren wir uns an Ihren Wünschen und Vorstellungen, sodass Sie nicht nur ein Qualitätsprodukt erhalten, sondern mit unserer Arbeit auch vollends zufrieden sind.</p>

  <div class="card" style="left:90px;width:245px">
    <svg width="70" height="60" viewBox="0 0 70 60" fill="#fff"><rect x="5" y="10" width="7" height="44" rx="3"/><rect x="16" y="10" width="7" height="44" rx="3"/><rect x="27" y="10" width="7" height="44" rx="3"/><rect x="38" y="10" width="7" height="44" rx="3"/><rect x="49" y="10" width="7" height="44" rx="3"/><rect x="60" y="22" width="4" height="20" fill="var(--red)"/></svg>
    <h3>Heizung</h3>
    <p>Vor allem in der kalten Jahreszeit ist eine Heizung unverzichtbar, denn sie garantiert Wärme</p>
    <span class="more">Mehr Lesen ⟶</span>
  </div>
  <div class="card red" style="left:353px;width:241px;height:355px">
    <svg width="70" height="60" viewBox="0 0 70 60" fill="#fff"><rect x="6" y="14" width="44" height="10"/><rect x="40" y="14" width="10" height="40"/><rect x="40" y="44" width="26" height="10"/><circle cx="20" cy="40" r="9" fill="none" stroke="#fff" stroke-width="3"/></svg>
    <h3>Dachklempnerei</h3>
    <p>Mit einem hohen Fachwissen führen wir alle klassischen</p>
    <span class="more">Mehr Lesen ⟶</span>
  </div>
  <div class="card" style="left:612px;width:244px">
    <svg width="70" height="60" viewBox="0 0 70 60"><circle cx="35" cy="30" r="26" fill="none" stroke="#fff" stroke-width="2" stroke-dasharray="4 3"/><path d="M35 12 L45 34 L30 34 Z" fill="var(--yellow)"/><circle cx="50" cy="20" r="7" fill="#fff"/></svg>
    <h3>Sanitar</h3>
    <p>Ruhe, Entspannung, Erholung und Hygiene – dies sind die Anforderungen unserer Gesellschaft an ein Badezimmer.</p>
    <span class="more">Mehr Lesen ⟶</span>
  </div>
  <div class="card" style="left:874px;width:243px;top:240px">
    <svg width="70" height="60" viewBox="0 0 70 60" fill="#fff"><path d="M8 8h54l-6 26H14z"/><rect x="32" y="34" width="6" height="20"/><rect x="20" y="52" width="30" height="4"/></svg>
    <h3>Alternative<br>Energien</h3>
    <p>Die Nachfrage nach alternativen Energien wächst stetig und auch wir bieten Ihnen umwelt</p>
    <span class="more">Mehr Lesen ⟶</span>
  </div>
  <i class="circle-btn" style="left:79px;top:408px"></i>
  <i class="circle-btn" style="left:1104px;top:408px"></i>
  <i class="abs" style="left:526px;top:617px;width:42px;height:5px;background:#fff;border-radius:3px"></i>
  <i class="abs" style="left:580px;top:617px;width:42px;height:5px;background:var(--blue);border-radius:3px"></i>
  <i class="abs" style="left:634px;top:617px;width:42px;height:5px;background:#fff;border-radius:3px"></i>
</section>

<!-- Referenzen -->
<section class="abs ref-band"></section>
<div class="abs photo" role="img" aria-label="Freigestelltes Foto: Handwerker in blauer Latzhose mit Rohrzange, Daumen hoch" style="left:115px;top:1946px;width:275px;height:431px;border-radius:120px 120px 0 0"></div>
<div class="abs sec-title" style="left:512px;top:2071px">Referenzen</div>
<div class="abs underline" style="left:512px;top:2116px;width:262px"></div>
<p class="abs ref-text">Bei uns sind Sie an der richtigen Stelle, wenn Sie auf der Suche nach hochwertigen und facettenreichen Klempnerleistungen sind. Seit 1989 ist unser Leistungsspektrum, ebenso wie unser Qualitätsanspruch, stetig gewachsen. Neben den gängigen Klempnerarbeiten realisieren die Mitarbeiter unseres Familienunternehmens exklusive Sanitär- und Heizungsinstallationen sowie vielseitige Dachklempnerarbeiten.</p>
<a class="btn abs" href="#" style="left:512px;top:2326px;width:346px;height:36px;line-height:36px;font-size:16px">Kontaktiere Uns Jetzt</a>

<!-- Partner -->
<i class="circle-btn" style="left:79px;top:2423px"></i>
<i class="partner" style="left:133px;width:106px"></i>
<i class="partner" style="left:283px;width:122px"></i>
<i class="partner" style="left:441px;width:146px"></i>
<i class="partner" style="left:620px;width:130px"></i>
<i class="partner" style="left:785px;width:118px"></i>
<i class="partner" style="left:938px;width:114px"></i>
<i class="circle-btn" style="left:1080px;top:2423px"></i>

<!-- Aktuelle Meldungen -->
<div class="abs sec-title" style="left:90px;top:2528px">Aktuelle Meldungen</div>
<a class="abs" href="#" style="left:972px;top:2534px;width:131px;height:44px;border:1.5px solid var(--blue);border-radius:5px;text-align:center;line-height:42px;font-size:14px;font-weight:700;color:var(--blue);text-decoration:none">Mehr Sehen</a>

<article class="news-card" style="left:90px;width:317px">
  <div class="img" role="img" aria-label="Foto: zwei Installateure tragen einen Heizkörper"></div>
  <div class="meta">Admin &nbsp;&nbsp;&nbsp; March 4, 2024 &nbsp;&nbsp;&nbsp; 0 Comments</div>
  <h3>Fortschrittliche Heizungsinnovation</h3>
  <p>Amet minim mollit non deserunt ullamco est sit aliqua dolor do amet sint. Velit officia consequat duis enim velit mollit.</p>
  <span class="more" style="top:438px">Mehr Lesen &nbsp;&nbsp;&nbsp;&nbsp;&nbsp;&nbsp;&nbsp; ›</span>
</article>
<article class="news-card" style="left:434px;width:332px">
  <div class="img" role="img" aria-label="Foto: Kundin und Installateur im Badezimmer"></div>
  <div class="meta">Admin &nbsp;&nbsp;&nbsp; March 4, 2024 &nbsp;&nbsp;&nbsp; 0 Comments</div>
  <h3>Sauberkeit Ohne Kompromisse</h3>
  <p>Amet minim mollit non deserunt ullamco est sit aliqua dolor do amet sint. Velit officia consequat duis enim velit mollit.</p>
  <span class="more" style="top:438px">Mehr Lesen &nbsp;&nbsp;&nbsp;&nbsp;&nbsp;&nbsp;&nbsp; ›</span>
</article>
<article class="news-card" style="left:782px;width:330px">
  <div class="img" role="img" aria-label="Foto: Monteur installiert Solarmodule auf einem Dach" style="background:linear-gradient(150deg,#c7d3e6,#3f5a9a)"></div>
  <div class="meta">Admin &nbsp;&nbsp;&nbsp; March 4, 2024 &nbsp;&nbsp;&nbsp; 0 Comments</div>
  <h3>Tipps Zum Energiesparen</h3>
  <p>Amet minim mollit non deserunt ullamco est sit aliqua dolor do amet sint. Velit officia consequat duis enim velit mollit.</p>
  <span class="more" style="top:438px;left:6px">Mehr Lesen &nbsp;&nbsp;&nbsp;&nbsp;&nbsp;&nbsp;&nbsp; ›</span>
</article>

<!-- Kontakt -->
<section class="abs contact">
  <div class="sec-title abs" style="left:97px;top:32px">Kontakt</div>
  <i class="ic" style="left:96px;top:97px"></i><div class="lbl" style="left:167px;top:94px">Telefon</div><div class="val" style="left:167px;top:118px">03721 480150</div>
  <i class="ic" style="left:390px;top:97px"></i><div class="lbl" style="left:456px;top:100px">Fax</div><div class="val" style="left:456px;top:122px">03721 480151</div>
  <i class="ic" style="left:96px;top:172px"></i><div class="lbl" style="left:167px;top:170px">Email</div><div class="val" style="left:167px;top:192px;text-decoration:underline">info@heizung-stolzke-beispiel.de</div>
  <i class="ic" style="left:96px;top:256px"></i><div class="lbl" style="left:167px;top:244px">Standort</div>
  <div class="val" style="left:167px;top:266px;line-height:26px;text-decoration:underline">Stolzke GmbH<br>Lindenweg 12<br>09399 Musterau OT Birkenhain</div>
  <p class="abs" style="left:97px;top:372px;width:640px;font-size:16px;line-height:20px;color:#444">Darüber hinaus steht Ihnen unsere Rufbereitschaft <b style="color:var(--blue)">unter 03721 480150</b> rund um die Uhr zur Verfügung, falls eines Ihrer Geräte einmal ausfallen sollte.</p>
</section>
<div class="abs photo" role="img" aria-label="Foto: Smartphone mit lächelndem Installateur im Videoanruf" style="left:738px;top:3153px;width:268px;height:485px;border-radius:34px;transform:rotate(6deg);background:linear-gradient(160deg,#dfe6f1,#5470b8)"></div>

<!-- Kontaktformular -->
<div class="form">
  <div class="abs sec-title" style="left:88px;top:3712px">Kontaktformular</div>
  <div class="small" style="left:87px;top:3769px;color:#888">gewünschter Rückruf-Zeitpunkt</div>
  <label style="left:87px;top:3806px">Name</label><div class="field" style="left:87px;top:3826px;width:240px">Enter your Vorname</div>
  <label style="left:338px;top:3806px">Telefon</label><div class="field" style="left:338px;top:3826px;width:248px">telefon</div>
  <label style="left:87px;top:3902px">Mail</label><div class="field" style="left:87px;top:3922px;width:238px">Johnexpqgm</div>
  <label style="left:338px;top:3902px">Fax</label><div class="field" style="left:338px;top:3922px;width:248px">Enter your Fax</div>
  <label style="left:87px;top:4000px">Ihre Nachricht an uns</label><div class="field" style="left:87px;top:4022px;width:499px;height:68px">Ihre Nachricht an uns</div>
  <i class="check" style="left:87px;top:4111px"></i><div class="small" style="left:117px;top:4107px">Kopie an die angegebene E-Mail schicken</div>
  <i class="check" style="left:87px;top:4143px"></i><div class="small" style="left:115px;top:4140px;width:480px">Ich habe die <u>Datenschutzerklärung</u> gelesen und stimme zu, dass meine zur Kontaktaufnahme und für Rückfragen übermittelten Angaben gemäß dieser Datenschutzerklärung verwendet werden.*</div>
  <div class="small" style="left:112px;top:4210px;width:430px">Ich kann meine Einwilligung jederzeit per E-Mail an <u>info@heizung-stolzke-beispiel.de</u> widerrufen.</div>
  <a class="btn abs" href="#" style="left:87px;top:4295px;width:494px;height:36px;line-height:36px;font-size:17px">Sender</a>
</div>
<div class="abs map" role="img" aria-label="Kartenausschnitt mit Standort der Klempnerei Stolzke und Umgebung">
  <div class="abs" style="left:14px;top:18px;width:330px;height:110px;background:#fff;border-radius:4px;padding:12px 18px;font-size:13px;color:#555">
    <b style="font-size:16px;color:#222">Lindenweg 12</b><br>Lindenweg 12, 09399<br>Musterau, Germany<br><span style="color:var(--blue);display:block;margin-top:12px">View larger map</span>
    <span class="abs" style="right:14px;top:42px;color:var(--blue)">Directions</span>
  </div>
</div>

<!-- Footer -->
<footer class="abs footer"></footer>
<div class="abs" style="left:173px;top:4424px">
  <div class="brand" style="color:#fff;font-size:32px"><span class="brand-dot"></span>Stolzke</div>
  <div class="tagline" style="color:#fff">Heizung · Sanitär · Bauklempnerei</div>
</div>
<i class="social" style="left:951px"></i><i class="social" style="left:1015px"></i><i class="social" style="left:1082px"></i><i class="social" style="left:1149px"></i>
<div class="abs" style="left:24px;top:4485px;width:1176px;height:4px;background:var(--red)"></div>
<div class="abs" style="left:24px;top:4489px;width:1176px;height:4px;background:var(--yellow)"></div>
<div class="abs" style="left:127px;top:4512px;width:85px;height:76px;background:#fff;border-radius:4px" role="img" aria-label="Innungszeichen"></div>
<div class="abs" style="left:227px;top:4510px;color:#fff">
  <div style="font-size:17px;font-weight:700">Meisterbetrieb Seit 1989</div>
  <div style="width:292px;height:4px;background:#cfd5ea;margin:8px 0 6px"></div>
  <div class="f-t">Mitglied der Innung SHK Musterkreis<br>und der Handwerkskammer Musterstadt</div>
</div>
<div class="abs" style="left:575px;top:4512px;color:#fff">
  <div class="f-h">STANDORT</div>
  <div class="f-t" style="margin-top:4px">Stolzke GmbH<br>Lindenweg 12<br>09399 Musterau OT<br>Birkenhain</div>
</div>
<div class="abs" style="left:871px;top:4507px;color:#fff">
  <div class="f-h">KONTAKT</div>
  <div class="f-t" style="margin-top:12px;line-height:20px">Telefon &nbsp;&nbsp;&nbsp;&nbsp;&nbsp;&nbsp; <b>03721 480150</b><br>Fax &nbsp;&nbsp;&nbsp;&nbsp;&nbsp;&nbsp;&nbsp;&nbsp;&nbsp;&nbsp;&nbsp;&nbsp; <b>03721 480151</b><br>E-Mail &nbsp;&nbsp;&nbsp;&nbsp;&nbsp;&nbsp; <b><u>info@heizung-stolzke-beispiel.de</u></b></div>
</div>
<div class="abs" style="left:322px;top:4640px;font-size:13px;color:#fff">© 2024 Heizung · Sanitär · Bauklempnerei Stolzke</div>
<div class="abs" style="left:744px;top:4640px;font-size:13px;color:#fff">Datenschutz &nbsp;&nbsp;&nbsp;&nbsp;&nbsp; Impressum</div>

</body>
</html>
```